The Hearth Guard Desk needs a Wordpress site for Home, Life and Safety Emergencies

NEED CUSTOM THEME FILES FOR WORDPRESS ncluded. I need a wordpress website that I will be able to edit down the road. Content wise the site I was trying to build is accurate. http://www.hearthguarddesk-example.com The site focuses on life, safety and home emergencies. My target audience is the first time home buyer. Usually in mid 20's think engineering type person.

I am up for a complete redesign. I want it to look clean and neat.

Things I need to have on the site :

- 2 Menus - A main menu and a secondary menu at top of page
- Search Bar in one of the main menus
- Social Media Share Buttons on one of the menus
- I am up for a color change (Maybe something a little softer) Need Help
- Main Page should be set up as a main page with separate blog page
- Need a CTA / Sign up for newsletter on page (location can vary)
- Blog Categories: When clicked need to show the full article and image.
- If you click on my home safety you will see how they are set up as a grid. I do not like this I want them to be easy to read and flow in order.

The site is going to mainly provide information for First Time Home Buyers. Eventually a page will be set up to sign up for a paid Home Safety Course. For now I want to focus on the content.

Mail should function with mail chimp for now.
This needs to be a functioning theme that I can edit. I currently have the rights to divi builder if that helps. I don't want to have to worry about the site I just want to focus on content creation.

Thank you

Target Market(s)

First Time Home Buyers Usually person in their 20's or 30's. Someone of the engineering, legal aid type mindset.

Industry/Entity Type

Safety

Coding

Coded - Design and coding required

Font styles to use
Serif
Sans Serif
Script

Colors

Designer to choose colors to be used in the design.

Requirements
Must have
• Wordpress integration.
• 2 Menus on top - Main and secondary
• Search function in a menu
• Social Media Icons in menu
• Sidebar with image of myself and some info on top , posts , categories
• Categories of blog posts need to list on the page. Not grid.
• Email signup on page at some part. (can be bottom, top or side. )
• Nice Clean state Front page.
• Color Combination that works well. (Doesn't have to be what is their now)
• Current links to site.
• Pulse Basics needs to be a link to an external site ( http://www.pulseclassroomharbor-example.com)
Nice to have
• I am flexible on the main page site design. I am not good at this so anything you feel. I cannot describe what I want but I will know it when I see it.
• I will come up with the information. Of course if any copy could be provided and shows value I would be willing to pay extra.
Should not have
• Grid Style for blog posts.
• Blog Posts should be in list style and each post for each category will just go down the page by order of date posted.

```html
<!DOCTYPE html>
<html lang="en">
<head>
<meta charset="utf-8">
<title>The Hearth Guard Desk – Home, Life and Safety Emergencies</title>
<link rel="stylesheet" href="https://fonts.googleapis.com/css2?family=Montserrat:wght@400;600;700;800&family=Open+Sans:wght@400;600;700&family=Kaushan+Script&display=swap">
<style>
:root{
  --red:#d9302b;
  --red-dark:#b8221e;
  --brown:#6b4a3a;
  --brown-dark:#4e3429;
  --ink:#2f2f2f;
  --muted:#777;
  --line:#e3e3e3;
  --white:#fff;
  --photo-warm:#c9b8a6;
}
*{box-sizing:border-box;margin:0;padding:0}
html,body{width:1200px;height:3508px;overflow:hidden}
body{font-family:"Open Sans",Arial,sans-serif;color:var(--ink);background:var(--white);position:relative}
a{color:inherit;text-decoration:none}
.abs{position:absolute}

/* top bar */
.topbar{top:0;left:0;width:1200px;height:48px;background:var(--brown);color:#f1e6e0;display:flex;align-items:center;padding:0 40px;font-size:12px}
.secondary-menu{display:flex;gap:26px}
.topbar-right{margin-left:auto;display:flex;align-items:center;gap:8px}
.social-dot{width:24px;height:24px;border-radius:50%;background:rgba(255,255,255,.22)}
.search{display:flex;margin-left:14px}
.search input{width:150px;height:26px;border:0;padding:0 8px;font-size:11px;font-family:inherit}
.search button{width:28px;height:26px;border:0;background:var(--red);display:flex;align-items:center;justify-content:center}

/* header */
.header{top:48px;left:0;width:1200px;height:112px;display:flex;align-items:center;padding:0 100px;border-bottom:1px solid var(--line)}
.brand{display:flex;align-items:center;gap:10px}
.brand-mark{width:22px;height:22px;background:var(--red)}
.brand-name{font-family:"Montserrat",sans-serif;font-weight:800;font-size:22px;line-height:1.05;color:var(--red);width:150px}
.main-menu{margin-left:auto;display:flex;font-family:"Montserrat",sans-serif;font-size:12px;font-weight:600;color:#555}
.main-menu a{padding:6px 18px;border-left:1px solid var(--line)}
.main-menu a:first-child{border-left:0}
.main-menu .active{color:var(--red);border-bottom:2px solid var(--red)}

/* hero */
.hero{top:160px;left:0;width:1200px;height:500px;background:linear-gradient(180deg,#5f5a57 0%,#8d8681 55%,#d9d5d1 100%);text-align:center;color:var(--white)}
.hero-title{margin-top:170px;font-family:"Montserrat",sans-serif;font-weight:800;font-size:56px;letter-spacing:1px}
.hero-tag{font-family:"Kaushan Script",cursive;font-size:32px;margin-top:6px}
.btn-red{display:inline-block;margin-top:22px;background:var(--red);color:var(--white);font-family:"Montserrat",sans-serif;font-weight:700;font-size:14px;padding:12px 30px;border-radius:22px}
.slider-arrow{width:30px;height:44px;background:rgba(0,0,0,.3);display:flex;align-items:center;justify-content:center}

/* intro */
.intro-photo{top:752px;left:100px;width:300px;height:330px;background:linear-gradient(135deg,#d8d2cb,#9aa3ad 60%,#3b4656)}
.intro-copy{top:760px;left:440px;width:640px}
.intro-copy h2{font-family:"Montserrat",sans-serif;font-size:18px;font-weight:700;line-height:1.6;margin-bottom:18px}
.ticks{list-style:none;font-size:14px;color:#555;line-height:1.55}
.ticks li{display:flex;gap:10px;margin-bottom:8px}
.ticks svg{flex:none;margin-top:3px}

/* services */
.services{top:1180px;left:0;width:1200px;height:600px;background:var(--red);clip-path:polygon(0 60px,100% 0,100% 520px,50% 600px,0 520px)}
.section-title{font-family:"Montserrat",sans-serif;font-weight:600;font-size:44px;text-align:center}
.title-rule{width:60px;height:3px;margin:12px auto 0}
.services .section-title{margin-top:118px;color:var(--white)}
.services .title-rule{background:var(--white)}
.service-card{top:1380px;width:306px;height:240px;box-shadow:0 6px 16px rgba(0,0,0,.25)}
.service-card .label{position:absolute;left:0;bottom:0;width:100%;height:44px;background:rgba(40,30,25,.72);color:var(--white);display:flex;align-items:center;justify-content:space-between;padding:0 16px;font-family:"Montserrat",sans-serif;font-weight:700;font-size:13px}
.btn-outline{top:1694px;left:510px;width:180px;height:40px;background:var(--white);color:var(--ink);font-family:"Montserrat",sans-serif;font-weight:700;font-size:12px;display:flex;align-items:center;justify-content:center;border-radius:3px}

/* categories */
.categories{top:1850px;left:0;width:1200px}
.categories .title-rule{background:var(--red)}
.cat{top:2000px;width:200px;text-align:center}
.cat-circle{width:104px;height:104px;border-radius:50%;background:var(--brown);margin:0 auto;display:flex;align-items:center;justify-content:center}
.cat-name{font-family:"Montserrat",sans-serif;font-weight:700;font-size:13px;margin-top:34px}
.cat-dot{width:12px;height:12px;border-radius:50%;background:var(--red);margin:12px auto 0}

/* recent posts */
.recent{top:2320px;left:0;width:1200px;height:680px;background:var(--red);clip-path:ellipse(120% 100% at 50% 100%)}
.recent .section-title{margin-top:96px;color:var(--white);font-weight:700;letter-spacing:1px}
.recent .title-rule{background:var(--white)}
.recent-lead{width:820px;margin:26px auto 0;text-align:center;color:#fde5e3;font-size:11px;line-height:1.7}
.post-card{top:2576px;width:240px;height:360px;background:var(--white);border-radius:120px 120px 6px 6px;overflow:hidden;text-align:center}
.post-photo{width:240px;height:200px;border-radius:120px 120px 0 0}
.post-card h3{font-family:"Montserrat",sans-serif;font-size:15px;font-weight:700;line-height:1.3;margin:18px 16px 8px}
.post-card p{font-size:11px;color:var(--muted);padding:0 18px}
.post-arrow{top:2740px;color:var(--white)}

/* footer */
.footer{top:3040px;left:0;width:1200px;height:424px}
.foot-col{top:3064px}
.foot-col h4{font-family:"Montserrat",sans-serif;font-size:15px;font-weight:700;margin-bottom:18px}
.foot-links{list-style:none;font-size:12px;color:#555;line-height:2.2}
.foot-links li::before{content:"›";color:var(--red);margin-right:8px;font-weight:700}
.contact-line{display:flex;gap:10px;font-size:12px;color:#555;line-height:1.6;margin-bottom:12px}
.newsletter p{font-size:11px;color:var(--muted);line-height:1.6;width:250px}
.newsletter input{margin-top:14px;width:250px;height:34px;border:1px solid var(--line);padding:0 10px;font-family:inherit;font-size:12px}
.newsletter .btn-sub{display:inline-block;margin-top:12px;background:var(--red);color:var(--white);font-family:"Montserrat",sans-serif;font-weight:700;font-size:12px;padding:9px 20px}
.foot-social{display:flex;gap:8px;margin-top:18px}
.foot-social span{width:28px;height:28px;border-radius:50%;background:var(--brown)}
.copyright{top:3464px;left:0;width:1200px;height:44px;background:var(--brown);color:#f1e6e0;font-size:12px;display:flex;align-items:center;justify-content:center}
</style>
</head>
<body>

<header>
  <div class="abs topbar">
    <nav class="secondary-menu">
      <a href="#">Home Safety</a><a href="#">Life Safety</a><a href="#">Fire Safety</a><a href="#">Get Safety</a><a href="#">Safety Saturday</a>
    </nav>
    <div class="topbar-right">
      <span class="social-dot"></span><span class="social-dot"></span><span class="social-dot"></span><span class="social-dot"></span><span class="social-dot"></span><span class="social-dot"></span>
      <form class="search">
        <input type="text" placeholder="Search ...">
        <button type="button" aria-label="Search"><svg width="13" height="13" viewBox="0 0 13 13"><circle cx="5.5" cy="5.5" r="4" fill="none" stroke="#fff" stroke-width="1.6"/><line x1="8.5" y1="8.5" x2="12" y2="12" stroke="#fff" stroke-width="1.6"/></svg></button>
      </form>
    </div>
  </div>

  <div class="abs header">
    <a class="brand" href="http://www.hearthguarddesk-example.com">
      <span class="brand-mark"></span>
      <span class="brand-name">THE HEARTH GUARD DESK</span>
    </a>
    <nav class="main-menu">
      <a class="active" href="#">HOME</a>
      <a href="#">ABOUT ME</a>
      <a href="#">SAFETY INFO</a>
      <a href="http://www.pulseclassroomharbor-example.com">PULSE BASICS</a>
      <a href="#">PREVENT HOME</a>
      <a href="#">DISASTERS</a>
      <a href="#">CONTACT ME</a>
    </nav>
  </div>
</header>

<section class="abs hero" role="img" aria-label="Hands sheltering paper cut-outs of a family, house and car">
  <h1 class="hero-title">THE HEARTH GUARD DESK</h1>
  <p class="hero-tag">Know Safety,Disaster Never Sleeps !</p>
  <a class="btn-red" href="#">Read More</a>
</section>
<div class="abs slider-arrow" style="top:390px;left:0"><svg width="10" height="16"><polyline points="8,2 2,8 8,14" fill="none" stroke="#fff" stroke-width="2"/></svg></div>
<div class="abs slider-arrow" style="top:390px;left:1170px"><svg width="10" height="16"><polyline points="2,2 8,8 2,14" fill="none" stroke="#fff" stroke-width="2"/></svg></div>

<section>
  <div class="abs intro-photo" role="img" aria-label="Man installing a smoke detector on a ceiling"></div>
  <div class="abs intro-copy">
    <h2>Want To Protect Your Home Or Loved One From An Emergency ?<br>Have You Had A Home Emergency ? Not Sure What To Do ?</h2>
    <ul class="ticks">
      <li><svg width="14" height="14"><polyline points="2,7 6,11 12,3" fill="none" stroke="#d9302b" stroke-width="2"/></svg>House Fires Kill 8 People every day.</li>
      <li><svg width="14" height="14"><polyline points="2,7 6,11 12,3" fill="none" stroke="#d9302b" stroke-width="2"/></svg>Flood damage accounts for $ 14.3 Billion in Property Damage Yearly.</li>
      <li><svg width="14" height="14"><polyline points="2,7 6,11 12,3" fill="none" stroke="#d9302b" stroke-width="2"/></svg>Be Prepared. Know What to do.</li>
      <li><svg width="14" height="14"><polyline points="2,7 6,11 12,3" fill="none" stroke="#d9302b" stroke-width="2"/></svg>As an Emergency Services Professional I want to share what I have seen and how to Help.</li>
      <li><svg width="14" height="14"><polyline points="2,7 6,11 12,3" fill="none" stroke="#d9302b" stroke-width="2"/></svg>We all have busy lives. Preparing NOW will Save you Time, Money and could Save A Life.</li>
    </ul>
  </div>
</section>

<section>
  <div class="abs services">
    <h2 class="section-title">Our Services</h2>
    <div class="title-rule"></div>
  </div>
  <div class="abs service-card" style="left:212px;background:linear-gradient(135deg,#8a8f98,#3f4650)" role="img" aria-label="Hands protecting a small model house">
    <div class="label">HOME SAFETY<svg width="12" height="12"><path d="M1 11 L3 7 L9 1 L11 3 L5 9 Z" fill="#fff"/></svg></div>
  </div>
  <div class="abs service-card" style="left:547px;background:linear-gradient(135deg,#9fc7e0,#3d7fb0)" role="img" aria-label="Paper cut-out family under sheltering hands">
    <div class="label">LIFE SAFETY<svg width="12" height="12"><path d="M1 11 L3 7 L9 1 L11 3 L5 9 Z" fill="#fff"/></svg></div>
  </div>
  <div class="abs service-card" style="left:882px;background:linear-gradient(135deg,#f3b04a,#c2361c 60%,#4a1c10)" role="img" aria-label="Fire extinguisher in front of flames">
    <div class="label">FIRE SAFETY<svg width="12" height="12"><path d="M1 11 L3 7 L9 1 L11 3 L5 9 Z" fill="#fff"/></svg></div>
  </div>
  <a class="abs btn-outline" href="#">VIEW MORE SERVICES</a>
</section>

<section>
  <div class="abs categories">
    <h2 class="section-title">Our Blog Categories</h2>
    <div class="title-rule"></div>
  </div>
  <div class="abs cat" style="left:80px">
    <div class="cat-circle"><svg width="40" height="44" viewBox="0 0 40 44"><rect x="12" y="12" width="16" height="30" rx="4" fill="#fff"/><rect x="16" y="4" width="8" height="8" fill="#fff"/><path d="M24 7 L34 5" stroke="#fff" stroke-width="3"/></svg></div>
    <div class="cat-name">FIRE SAFETY</div><div class="cat-dot"></div>
  </div>
  <div class="abs cat" style="left:368px">
    <div class="cat-circle"><svg width="44" height="44" viewBox="0 0 44 44"><path d="M6 30 Q6 16 16 14 L16 28 Z M38 30 Q38 16 28 14 L28 28 Z" fill="#fff"/><path d="M22 10 L30 18 L14 18 Z" fill="#fff"/></svg></div>
    <div class="cat-name">HOME SAFETY TIPS</div><div class="cat-dot"></div>
  </div>
  <div class="abs cat" style="left:620px">
    <div class="cat-circle"><svg width="40" height="44" viewBox="0 0 40 44"><path d="M20 3 L36 9 L36 22 Q36 36 20 42 Q4 36 4 22 L4 9 Z" fill="none" stroke="#fff" stroke-width="3"/><polyline points="12,22 18,28 28,16" fill="none" stroke="#fff" stroke-width="3"/></svg></div>
    <div class="cat-name">SAFETY SATURDAY POSTS</div><div class="cat-dot"></div>
  </div>
  <div class="abs cat" style="left:892px">
    <div class="cat-circle"><svg width="40" height="40" viewBox="0 0 40 40"><path d="M14 4 L11 36 M28 4 L25 36 M5 14 H36 M4 26 H35" stroke="#fff" stroke-width="3.5"/></svg></div>
    <div class="cat-name">UNCATEGORIZED</div><div class="cat-dot"></div>
  </div>
</section>

<section>
  <div class="abs recent">
    <h2 class="section-title">RECENT POSTS</h2>
    <div class="title-rule"></div>
    <p class="recent-lead">Small steps taken today keep a first home safe tomorrow. Read our latest notes on alarms, escape plans, basic first aid and getting ready before trouble starts, written plainly for new owners who like to know how things work.</p>
  </div>
  <div class="abs post-arrow" style="left:40px"><svg width="12" height="20"><polyline points="10,2 2,10 10,18" fill="none" stroke="#fff" stroke-width="2"/></svg></div>
  <div class="abs post-arrow" style="left:1148px"><svg width="12" height="20"><polyline points="2,2 10,10 2,18" fill="none" stroke="#fff" stroke-width="2"/></svg></div>

  <article class="abs post-card" style="left:120px">
    <div class="post-photo" role="img" aria-label="Firefighter in front of a burning building" style="background:linear-gradient(160deg,#f0a03a,#a52a14 60%,#2a140e)"></div>
    <h3>Safety Saturday<br>Escape Plan</h3><p>Map two ways out of every room.</p>
  </article>
  <article class="abs post-card" style="left:368px">
    <div class="post-photo" role="img" aria-label="Hand testing a ceiling smoke detector" style="background:linear-gradient(160deg,#e6e6e6,#a7adb4)"></div>
    <h3>Safety Saturday<br>Smoke Detector</h3><p>Test each alarm once a month.</p>
  </article>
  <article class="abs post-card" style="left:616px">
    <div class="post-photo" role="img" aria-label="Chest compressions practised on a training dummy" style="background:linear-gradient(160deg,#c4d3de,#6a7f93)"></div>
    <h3>Pulse Basics</h3><p>Hands-only steps anyone can learn.</p>
  </article>
  <article class="abs post-card" style="left:864px">
    <div class="post-photo" role="img" aria-label="Fire extinguisher aimed at a small house fire" style="background:linear-gradient(160deg,#f2c1b6,#d9302b 70%,#7a1a14)"></div>
    <h3>Plan your Fire Escape<br>Surviving a House Fire</h3><p>Stay low and get out fast.</p>
  </article>
</section>

<footer>
  <div class="abs foot-col" style="left:100px;width:240px">
    <div class="brand" style="margin-bottom:26px">
      <span class="brand-mark"></span>
      <span class="brand-name">THE HEARTH GUARD DESK</span>
    </div>
    <div class="contact-line"><svg width="12" height="16" viewBox="0 0 12 16"><path d="M6 1 A5 5 0 0 1 11 6 C11 10 6 15 6 15 C6 15 1 10 1 6 A5 5 0 0 1 6 1 Z" fill="#d9302b"/><circle cx="6" cy="6" r="2" fill="#fff"/></svg><span>1420 Cedar Ridge Lane,<br>Maple Hollow, ST 00412</span></div>
    <div class="contact-line"><svg width="14" height="14" viewBox="0 0 14 14"><path d="M3 1 L5 1 L6 4 L4.5 5.5 Q6 8.5 8.5 9.5 L10 8 L13 9 L13 11 Q13 13 11 13 Q1 12 1 3 Q1 1 3 1 Z" fill="#d9302b"/></svg><span>Phone: (555) 014-2290</span></div>
    <div class="contact-line"><svg width="14" height="12" viewBox="0 0 14 12"><rect x="1" y="1" width="12" height="10" fill="none" stroke="#d9302b" stroke-width="1.5"/><polyline points="1,1 7,7 13,1" fill="none" stroke="#d9302b" stroke-width="1.5"/></svg><span>Email : hello@hearthguarddesk-example.com</span></div>
  </div>

  <div class="abs foot-col" style="left:400px">
    <h4>Quick Links</h4>
    <ul class="foot-links"><li>Home</li><li>About Us</li><li>Safety Info</li><li>Pulse Basics</li><li>Disasters</li><li>Contact Me</li><li>Prevent Home</li></ul>
  </div>
  <div class="abs foot-col" style="left:620px">
    <h4>Other Links</h4>
    <ul class="foot-links"><li>Privacy policy</li><li>Local Activities</li><li>Information</li><li>Directions &amp; Maps</li><li>Contact Us</li><li>Services</li></ul>
  </div>
  <div class="abs foot-col newsletter" style="left:830px">
    <h4>Subscribe To Newsletter</h4>
    <p>Get short safety tips and new posts in your inbox each week. No spam, unsubscribe at any time.</p>
    <input type="email" placeholder="Email">
    <br><a class="btn-sub" href="#">SUBSCRIBE</a>
    <div class="foot-social"><span></span><span></span><span></span><span></span><span></span></div>
  </div>

  <div class="abs copyright">© Copyright 2017 The Hearth Guard Desk . All Rights Reserved.</div>
</footer>

</body>
</html>
```